Brisco Beverage Co.

Brisco is a new beverage company that currently specializes in energy and hydration. I need label design for the bottles. The label will be a full sleeve so free free to use the entire bottle. The premise behind the product is that its a Brisco from the competition. The label needs to say smart, strong, expensive. The background for the label will be black.
Updates

I need an entire label design as well as logo

Target Market(s)

20-30 year old active people.

Industry/Entity Type

It Company

Logo Text

By athletes for the athlete in all of us.

Logo styles of interest
Pictorial/Combination Logo
Wordmark Logo
Requirements
Must have
• the flavors are fruit based. Blackberry lime, mango pineapple, mango berry, strawberry kiwi. Incorporate natural looking fruit into the design.

```html
<!DOCTYPE html>
<html lang="en">
<head>
<meta charset="utf-8">
<title>Brisco Natural Energy – Blackberry Lime Sleeve Label</title>
<link href="https://fonts.googleapis.com/css2?family=Archivo+Black&family=Orbitron:wght@700;900&display=swap" rel="stylesheet">
<style>
  :root {
    --page: #ffffff;
    --sleeve-black: #050505;
    --brush-silver: #e2e2e2;
    --brush-grey: #8e8e8e;
    --brand-green: #7dc13b;
    --lime-bright: #8ccf45;
    --lime-mid: #4f8a22;
    --lime-dark: #1d3010;
    --flavor-box: #f2f2f2;
    --ink: #111111;
  }
  html, body {
    margin: 0;
    padding: 0;
    width: 1200px;
    height: 2837px;
    overflow: hidden;
    background: var(--page);
  }
  .canvas {
    position: relative;
    width: 1200px;
    height: 2837px;
    overflow: hidden;
  }
  .sleeve-shape {
    position: absolute;
    left: 0;
    top: 0;
  }
  .brush-splash {
    position: absolute;
    left: 400px;
    top: 1250px;
    width: 380px;
    height: 560px;
    border-radius: 18px;
    background: linear-gradient(160deg, var(--brush-silver) 0%, #bdbdbd 40%, var(--brush-grey) 75%, #3a3a3a 100%);
  }
  .fruit-photo {
    position: absolute;
    left: 380px;
    top: 1700px;
    width: 360px;
    height: 460px;
    border-radius: 18px;
    background: linear-gradient(180deg, var(--lime-bright) 0%, var(--lime-mid) 35%, var(--lime-dark) 75%, #0b0f08 100%);
  }
  .brand-name {
    position: absolute;
    left: 140px;
    width: 880px;
    top: 1430px;
    text-align: center;
    font-family: "Orbitron", sans-serif;
    font-weight: 900;
    font-size: 150px;
    letter-spacing: 8px;
    color: var(--brand-green);
    line-height: 1;
    white-space: nowrap;
  }
  .brand-tagline {
    position: absolute;
    left: 300px;
    width: 420px;
    top: 1600px;
    text-align: center;
    font-family: "Orbitron", sans-serif;
    font-weight: 700;
    font-size: 28px;
    letter-spacing: 4px;
    color: var(--brand-green);
    white-space: nowrap;
  }
  .flavor-tag {
    position: absolute;
    left: 250px;
    top: 1665px;
    width: 540px;
    height: 96px;
    box-sizing: border-box;
    background: linear-gradient(180deg, #ffffff, var(--flavor-box) 60%, #cfcfcf);
    transform: rotate(-7deg);
    display: flex;
    align-items: center;
    justify-content: center;
    font-family: "Archivo Black", sans-serif;
    font-size: 42px;
    color: var(--ink);
    white-space: nowrap;
  }
  .flavor-tag .flavor-accent { color: var(--brand-green); margin-left: 14px; }
  .volume {
    position: absolute;
    left: 0;
    width: 1200px;
    top: 2370px;
    text-align: center;
    font-family: "Orbitron", sans-serif;
    font-weight: 700;
    font-size: 26px;
    letter-spacing: 2px;
    color: var(--brand-green);
  }
</style>
</head>
<body>
<main class="canvas">
  <svg class="sleeve-shape" width="1200" height="2837" viewBox="0 0 1200 2837" aria-hidden="true">
    <defs>
      <linearGradient id="dome-fade" x1="0" y1="0" x2="0" y2="1">
        <stop offset="0" stop-color="#9a9a9a"/>
        <stop offset="0.4" stop-color="#454545"/>
        <stop offset="1" stop-color="#050505"/>
      </linearGradient>
      <linearGradient id="band" x1="0" y1="0" x2="0" y2="1">
        <stop offset="0" stop-color="#eeeeef"/>
        <stop offset="0.5" stop-color="#c9cacc"/>
        <stop offset="1" stop-color="#e4e4e6"/>
      </linearGradient>
    </defs>
    <path class="sleeve-body" fill="var(--sleeve-black)"
      d="M330 500 L870 500 C990 540 1080 700 1090 900 L1090 1060 C1085 1090 1030 1100 1030 1120 C1030 1140 1095 1160 1100 1190 L1100 2450 L105 2450 L105 1190 C110 1160 170 1140 170 1120 C170 1100 115 1090 110 1060 L110 900 C120 700 210 540 330 500 Z"/>
    <path class="halftone-fade" role="img" aria-label="Halftone dot pattern fading down the shoulder" fill="url(#dome-fade)" opacity="0.85"
      d="M330 500 L870 500 C990 540 1080 700 1090 900 L1090 1120 L110 1120 L110 900 C120 700 210 540 330 500 Z"/>
    <rect class="base-band" x="105" y="2450" width="995" height="110" fill="url(#band)"/>
  </svg>

  <div class="brush-splash" role="img" aria-label="Silver paint brush splash behind the brand name"></div>
  <div class="fruit-photo" role="img" aria-label="Photograph of sliced limes and blackberries fading into black"></div>

  <div class="brand-name">BRISCO</div>
  <div class="brand-tagline">NATURAL ENERGY</div>

  <div class="flavor-tag">BLACKBERRY<span class="flavor-accent">LIME</span></div>

  <div class="volume">24 FL . OZ (710) mL</div>
</main>
</body>
</html>
```